Now Open Poster

We need a banner for our sports supplement and nutritional store, Harbor Nutrition.
We were hoping for some sort of creative word art piece.
I have drawn my own mock up just to give you all a very basic starting point. But you are free to go with whatever you feel will work best.
The primary objective is simply to explain a little about what the company does, and then direct traffic towards the store with an 'Open Arrow' pointing left.
Text words we have chosen are:
Protein
Creatine
Health
Fitness
Sports Science
Nutrition
Energy
Achievement
Amino Acids
Organic
Supplements
Performance
Testosterone Support
Vitamins
Growth
Diet
Happiness
Weight Loss
Strong
Natural
Vitality
Accomplished
Below the word art we want our logo (See attached options)
Then below the logo the phrase "Success Starts Here"
Dimensions of the poster are 140cm x 60cm.
Colours: Blues/Whites/Greys/Blacks (Lots of white space please)
Here are some cool pieces I found that had some interesting elements that I liked (I'd love to see a mash-up of styles with a street art feel to it. Something funky!):
http://www.moodwall-example.com/pin/100000000000000001/
http://www.moodwall-example.com/pin/100000000000000002/
http://www.moodwall-example.com/pin/100000000000000003/
http://www.moodwall-example.com/pin/100000000000000004/
http://www.moodwall-example.com/pin/100000000000000005/
Thanks for reading, message me if you have any further questions!
- Tobias

```html
<!DOCTYPE html>
<html lang="en">
<head>
<meta charset="utf-8">
<title>Harbor Nutrition – Now Open</title>
<link rel="stylesheet" href="https://fonts.googleapis.com/css2?family=Anton&family=Archivo+Black&family=Cabin+Sketch:wght@700&family=Dancing+Script:wght@700&family=Great+Vibes&family=Montserrat:wght@800&family=Oswald:wght@700&family=Playfair+Display:ital,wght@0,400;0,700;1,400;1,700&family=Poppins:wght@600;700&family=Racing+Sans+One&family=Rye&family=Yellowtail&display=swap">
<style>
  :root {
    --ink: #161616;
    --blue: #2c62a3;
    --blue-deep: #1f4f8f;
    --navy: #2d4d7a;
    --grey: #8b8b8b;
    --grey-mid: #a6a6a6;
    --grey-light: #c9c9c9;
    --paper: #ffffff;
  }
  html, body { margin: 0; padding: 0; background: var(--paper); overflow: hidden; width: 1200px; height: 2599px; }
  .poster { display: block; width: 1200px; height: 2599px; background: var(--paper); }
  .open-word { font-family: "Poppins", sans-serif; font-weight: 700; fill: var(--ink); }
  .sketch { font-family: "Cabin Sketch", cursive; font-weight: 700; }
  .script-thin { font-family: "Great Vibes", "Dancing Script", cursive; }
  .script-brush { font-family: "Yellowtail", "Dancing Script", cursive; }
  .script-bold { font-family: "Dancing Script", "Yellowtail", cursive; font-weight: 700; }
  .serif { font-family: "Playfair Display", serif; }
  .serif-italic { font-family: "Playfair Display", serif; font-style: italic; }
  .block { font-family: "Archivo Black", sans-serif; }
  .condensed { font-family: "Anton", sans-serif; }
  .condensed-alt { font-family: "Oswald", sans-serif; font-weight: 700; }
  .western { font-family: "Rye", serif; }
  .racing { font-family: "Racing Sans One", sans-serif; }
  .headline { font-family: "Poppins", sans-serif; font-weight: 600; fill: var(--ink); }
  .tagline { font-family: "Montserrat", sans-serif; font-weight: 800; fill: var(--blue-deep); }
  .fill-ink { fill: var(--ink); }
  .fill-blue { fill: var(--blue); }
  .fill-deep { fill: var(--blue-deep); }
  .fill-navy { fill: var(--navy); }
  .fill-grey { fill: var(--grey); }
  .fill-grey-mid { fill: var(--grey-mid); }
  .fill-grey-light { fill: var(--grey-light); }
  .fill-paper { fill: var(--paper); }
  .rule { stroke: var(--ink); stroke-width: 4; }
  .brand-name { font-family: "Playfair Display", serif; font-weight: 700; fill: var(--ink); }
</style>
</head>
<body>
<svg class="poster" viewBox="0 0 1200 2599" xmlns="http://www.w3.org/2000/svg">
  <defs>
    <linearGradient id="crownTone" x1="0" y1="0" x2="0" y2="1">
      <stop offset="0" stop-color="#3a3a3a"/>
      <stop offset="1" stop-color="#111111"/>
    </linearGradient>
    <linearGradient id="athleteTone" x1="0" y1="0" x2="0" y2="1">
      <stop offset="0" stop-color="#d6d6d6"/>
      <stop offset="0.6" stop-color="#7a7a7a"/>
      <stop offset="1" stop-color="#3a3a3a"/>
    </linearGradient>
  </defs>

  <g class="open-arrows fill-ink">
    <polygon points="165,44 165,132 110,88"/>
    <polygon points="220,44 220,132 165,88"/>
    <polygon points="930,44 930,132 875,88"/>
    <polygon points="985,44 985,132 930,88"/>
  </g>
  <text class="open-word" x="600" y="132" text-anchor="middle" font-size="110" textLength="470" lengthAdjust="spacingAndGlyphs">OPEN</text>

  <g class="crown-rules">
    <line class="rule" x1="58" y1="230" x2="470" y2="230"/>
    <line class="rule" x1="730" y1="230" x2="1142" y2="230"/>
    <circle cx="50" cy="230" r="9" fill="none" stroke="var(--ink)" stroke-width="4"/>
    <circle cx="1150" cy="230" r="9" fill="none" stroke="var(--ink)" stroke-width="4"/>
  </g>
  <rect role="img" aria-label="Ornamental crown illustration" x="500" y="172" width="200" height="175" rx="6" fill="url(#crownTone)"/>

  <text class="sketch fill-ink" x="136" y="338" font-size="78" textLength="314" lengthAdjust="spacingAndGlyphs">START</text>
  <text class="sketch fill-ink" x="830" y="338" font-size="78" textLength="210" lengthAdjust="spacingAndGlyphs">NOW</text>

  <text class="script-bold fill-grey" x="208" y="435" font-size="72" textLength="124" lengthAdjust="spacingAndGlyphs">be fit</text>
  <text class="block fill-grey-light" x="395" y="490" font-size="128" textLength="552" lengthAdjust="spacingAndGlyphs">PROTEIN</text>
  <text class="serif-italic fill-grey" x="154" y="560" font-size="120" textLength="420" lengthAdjust="spacingAndGlyphs">Creatine</text>

  <path role="img" aria-label="Lightning bolt" class="fill-ink" d="M1080,450 L1130,450 L1110,510 L1136,510 L1092,618 L1098,545 L1072,545 Z"/>
  <text class="script-brush fill-blue" x="660" y="660" font-size="170" textLength="410" lengthAdjust="spacingAndGlyphs">Health</text>
  <text class="condensed fill-deep" x="130" y="728" font-size="155" textLength="505" lengthAdjust="spacingAndGlyphs">WEIGHTLOSS</text>
  <text class="script-bold fill-ink" x="705" y="772" font-size="78" textLength="395" lengthAdjust="spacingAndGlyphs">Supplements</text>

  <text class="script-bold fill-ink" x="66" y="822" font-size="88" textLength="200" lengthAdjust="spacingAndGlyphs">Happi</text>
  <text class="script-bold fill-ink" x="288" y="868" font-size="60" textLength="96" lengthAdjust="spacingAndGlyphs">ness</text>
  <text class="racing fill-grey-mid" x="405" y="872" font-size="150" textLength="250" lengthAdjust="spacingAndGlyphs" transform="skewX(-8) translate(120 0)">DIET</text>

  <g class="amino-acids">
    <rect x="675" y="805" width="180" height="66" class="fill-grey-mid"/>
    <rect x="865" y="805" width="195" height="66" class="fill-grey-mid"/>
    <text class="condensed-alt fill-paper" x="688" y="861" font-size="62" textLength="154" lengthAdjust="spacingAndGlyphs">AMINO</text>
    <text class="condensed-alt fill-paper" x="878" y="861" font-size="62" textLength="169" lengthAdjust="spacingAndGlyphs">ACIDS</text>
  </g>
  <line class="rule" x1="1116" y1="790" x2="1116" y2="1215" stroke-width="6"/>

  <text class="serif fill-grey" x="143" y="950" font-size="100" textLength="190" lengthAdjust="spacingAndGlyphs">I am</text>
  <path role="img" aria-label="Heart" class="fill-ink" d="M162,1085 C130,1055 105,1035 105,1005 C105,985 120,975 135,975 C148,975 158,983 162,995 C166,983 176,975 189,975 C204,975 220,985 220,1005 C220,1035 194,1055 162,1085 Z"/>
  <text class="serif-italic fill-blue" x="240" y="1080" font-size="170" font-weight="700" textLength="395" lengthAdjust="spacingAndGlyphs">closer</text>
  <text class="condensed-alt fill-grey" x="655" y="1092" font-size="200" textLength="440" lengthAdjust="spacingAndGlyphs">VITAMINS</text>

  <rect x="184" y="1100" width="34" height="310" class="fill-grey-mid"/>
  <text class="serif fill-deep" x="240" y="1218" font-size="115" textLength="155" lengthAdjust="spacingAndGlyphs">am</text>
  <text class="sketch fill-ink" x="438" y="1212" font-size="130" textLength="637" lengthAdjust="spacingAndGlyphs">OrGANiC</text>

  <text class="condensed fill-grey-mid" x="242" y="1410" font-size="200" textLength="485" lengthAdjust="spacingAndGlyphs">BETTER</text>
  <text class="serif fill-ink" x="740" y="1400" font-size="190" textLength="46" lengthAdjust="spacingAndGlyphs">}</text>
  <text class="sketch fill-grey" x="826" y="1322" font-size="78" textLength="330" lengthAdjust="spacingAndGlyphs">TODAY</text>
  <text class="script-brush fill-blue" x="840" y="1432" font-size="115" textLength="300" lengthAdjust="spacingAndGlyphs">Vitality</text>

  <text class="serif fill-ink" x="68" y="1590" font-size="190" textLength="50" lengthAdjust="spacingAndGlyphs">{</text>
  <text class="sketch fill-ink" x="127" y="1515" font-size="72" textLength="92" lengthAdjust="spacingAndGlyphs">NA</text>
  <text class="serif-italic fill-grey" x="232" y="1515" font-size="72" textLength="110" lengthAdjust="spacingAndGlyphs">than</text>
  <text class="racing fill-grey" x="440" y="1525" font-size="115" textLength="410" lengthAdjust="spacingAndGlyphs">yesterday</text>
  <text class="sketch fill-ink" x="132" y="1612" font-size="88" textLength="650" lengthAdjust="spacingAndGlyphs">TURAL HERBS</text>

  <rect role="img" aria-label="Vintage strongman lifting a barbell overhead" x="885" y="1480" width="260" height="380" fill="url(#athleteTone)"/>
  <rect x="837" y="1862" width="308" height="58" class="fill-ink"/>
  <text class="condensed-alt fill-paper" x="850" y="1905" font-size="44" textLength="282" lengthAdjust="spacingAndGlyphs">PERFORMANCE</text>

  <text class="script-bold fill-grey-light" x="112" y="1700" font-size="74" textLength="108" lengthAdjust="spacingAndGlyphs">live</text>
  <text class="script-bold fill-grey-light" x="168" y="1782" font-size="74" textLength="160" lengthAdjust="spacingAndGlyphs">well</text>
  <text class="western fill-deep" x="363" y="1772" font-size="150" textLength="550" lengthAdjust="spacingAndGlyphs">NUTRITION</text>

  <text class="racing fill-grey" x="66" y="1884" font-size="110" textLength="340" lengthAdjust="spacingAndGlyphs">ENERGY</text>
  <text class="serif fill-grey" x="430" y="1900" font-size="108" textLength="363" lengthAdjust="spacingAndGlyphs">Growth</text>
  <text class="serif-italic fill-navy" x="209" y="1992" font-size="124" textLength="612" lengthAdjust="spacingAndGlyphs">achievement</text>
  <text class="script-thin fill-grey-light" x="903" y="1995" font-size="84" textLength="177" lengthAdjust="spacingAndGlyphs">fitness</text>

  <text class="headline" x="143" y="2147" font-size="140" textLength="957" lengthAdjust="spacingAndGlyphs">I AM HARBOR</text>

  <g class="brand-mark">
    <circle cx="600" cy="2323" r="153" fill="none" stroke="var(--ink)" stroke-width="3"/>
    <text class="brand-name" x="600" y="2313" text-anchor="middle" font-size="46">HARBOR</text>
    <text class="brand-name" x="600" y="2361" text-anchor="middle" font-size="34">NUTRITION</text>
  </g>

  <text class="tagline" x="136" y="2578" font-size="80" textLength="956" lengthAdjust="spacingAndGlyphs">SUCCESS STARTS HERE.</text>
</svg>
</body>
</html>
```